Web design for construction/ handyman company. We are a new company and trying to brand ourselves.

We have a logo with a character already in place and want a user friendly and simple site. I'm attaching our logo designs with our Crocodile character to get an idea of our logo. We want people to remember us and our site. The name we chose was so we could use a logo with a character. Our name is Pelican Builders LLC.

Target Market(s)

New clients

Industry/Entity Type

Contractor

Coding

Coded - Design and coding required

Number of Pages Required

4 page

Font styles to use
Sans Serif

Requirements
Must have
• About Us Page, What we do (not sure what to call this), Contact Us, Home Page. Would like the same colors as on our business card designs to be used on the website.
Nice to have
• We eventually want a project page to add photos of projects but thats not necessary now. Would be nice to use the crocodile theme, hammer or something similar somehow in the page names or clicks.

```html
<!DOCTYPE html>
<html lang="en">
<head>
<meta charset="utf-8">
<title>Pelican Builders LLC</title>
<link href="https://fonts.googleapis.com/css2?family=Open+Sans:wght@400;600;700&family=Raleway:wght@300;400;600&display=swap" rel="stylesheet">
<style>
:root{
  --blue:#1d5ea8;
  --blue-dark:#174d8c;
  --green:#6cb52d;
  --green-dark:#4f8f1c;
  --text:#333;
  --muted:#666;
  --line:#cfd6de;
  --bg:#ffffff;
}
*{box-sizing:border-box;margin:0;padding:0}
html,body{width:732px;height:1200px;overflow:hidden;background:var(--bg);font-family:"Open Sans",Arial,sans-serif;color:var(--text)}
.page{position:relative;width:732px;height:1200px;overflow:hidden}
.header{position:absolute;top:0;left:0;width:732px;height:104px}
.brand{position:absolute;left:56px;top:28px;display:flex;align-items:center;gap:10px;font-weight:700;font-size:22px;color:var(--green-dark);white-space:nowrap}
.brand-dot{width:34px;height:34px;border-radius:50%;background:var(--blue)}
.contact-top{position:absolute;top:62px;right:48px;display:flex;gap:36px;font-size:15px;color:var(--blue);white-space:nowrap}
.contact-top span{display:flex;align-items:center;gap:8px}
.nav{position:absolute;top:112px;left:56px;width:620px;height:32px;background:var(--blue);display:flex;align-items:center}
.nav a{color:#fff;text-decoration:none;font-size:12px;padding:0 20px;height:32px;line-height:32px;white-space:nowrap}
.nav a.active{background:var(--green)}
.search{position:absolute;right:6px;top:5px;width:170px;height:22px;background:#fff;font-size:10px;color:#888;padding:4px 6px;display:flex;justify-content:space-between;align-items:center}
.hero{position:absolute;top:150px;left:56px;width:620px;height:292px;background:linear-gradient(135deg,#e8e6e1,#bdb4a6 55%,#6f6558)}
.dots{position:absolute;top:452px;left:0;width:732px;display:flex;justify-content:center;gap:8px}
.dots i{width:9px;height:9px;border-radius:50%;background:#555}
.section-title{position:absolute;top:478px;left:56px;width:620px;display:flex;align-items:center;gap:14px;font-family:"Raleway",sans-serif;font-weight:300;font-size:32px;color:var(--green-dark);white-space:nowrap}
.section-title::before,.section-title::after{content:"";flex:1;height:1px;background:var(--line)}
.service{position:absolute;top:536px;width:180px;text-align:center}
.service .photo{height:98px}
.service h3{margin-top:14px;font-family:"Raleway",sans-serif;font-weight:400;font-size:16px;color:var(--green-dark);white-space:nowrap}
.service p{margin-top:6px;font-size:9.5px;line-height:1.45;color:var(--muted)}
.welcome{position:absolute;top:752px;left:56px;width:420px;height:240px}
.welcome h2{font-family:"Raleway",sans-serif;font-weight:600;font-size:20px;color:var(--blue);white-space:nowrap}
.mascot{position:absolute;top:40px;left:0;width:140px;height:160px;background:radial-gradient(circle at 50% 50%,#7fbf4a,#d9e9c8 70%,#fff)}
.welcome .intro{position:absolute;top:40px;left:152px;width:268px;font-size:10px;line-height:1.55;color:var(--muted)}
.checks{position:absolute;top:136px;left:152px;width:268px;display:grid;grid-template-columns:1fr 1fr;gap:5px 10px;font-size:10px;color:var(--muted)}
.checks li{list-style:none;display:flex;align-items:center;gap:6px;white-space:nowrap}
.read-more{position:absolute;top:204px;right:0;background:var(--green-dark);color:#fff;font-size:11px;padding:5px 10px;white-space:nowrap}
.quote{position:absolute;top:752px;left:496px;width:180px;height:232px;background:var(--green)}
.quote h4{background:var(--green-dark);color:#fff;text-align:center;padding:8px 0 6px;font-size:11px;font-weight:400;line-height:1.2;white-space:nowrap}
.quote h4 b{display:block;font-family:"Raleway",sans-serif;font-weight:400;font-size:20px}
.quote .field{margin:7px 12px 0;background:#fff;height:20px;font-size:9px;color:#888;padding:4px 6px}
.quote .field.tall{height:52px}
.quote .submit{display:block;margin:8px auto 0;width:66px;background:var(--blue);color:#fff;text-align:center;font-size:11px;padding:4px 0}
.footer{position:absolute;top:1008px;left:0;width:732px;height:192px;background:var(--blue)}
.footer-nav{position:absolute;top:28px;left:56px;display:flex;align-items:center;gap:20px;font-size:12px;color:#fff;white-space:nowrap}
.footer-nav .pill{border:1px solid #fff;border-radius:14px;padding:3px 14px}
.social{position:absolute;top:32px;right:56px;display:flex;gap:24px}
.footer-rule{position:absolute;top:64px;left:56px;width:620px;height:1px;background:rgba(255,255,255,.35)}
.footer h5{position:absolute;top:80px;left:86px;font-family:"Raleway",sans-serif;font-weight:400;font-size:16px;color:#fff}
.footer-row{position:absolute;top:108px;left:56px;width:620px;display:flex;align-items:center;gap:12px;font-size:8px;line-height:1.4;color:#dce7f4;white-space:nowrap}
.footer-row .item{display:flex;align-items:center;gap:6px}
.footer-row .ico{width:22px;height:22px;border-radius:50%;background:#fff;display:flex;align-items:center;justify-content:center;flex:none}
.footer-row .copy{margin-left:auto}
</style>
</head>
<body>
<div class="page">
  <header class="header">
    <div class="brand"><span class="brand-dot"></span>Pelican Builders LLC</div>
    <div class="contact-top">
      <span><svg width="16" height="16" viewBox="0 0 24 24"><path fill="#6cb52d" d="M6.6 10.8a15 15 0 0 0 6.6 6.6l2.2-2.2c.3-.3.7-.4 1-.2 1.1.4 2.3.6 3.6.6.6 0 1 .4 1 1V20c0 .6-.4 1-1 1A17 17 0 0 1 3 4c0-.6.4-1 1-1h3.5c.6 0 1 .4 1 1 0 1.3.2 2.5.6 3.6.1.3 0 .7-.2 1z"/></svg>123 456 7890</span>
      <span><svg width="18" height="14" viewBox="0 0 24 18"><rect x="1" y="1" width="22" height="16" fill="none" stroke="#1d5ea8" stroke-width="2"/><path d="M1 1l11 9 11-9" fill="none" stroke="#1d5ea8" stroke-width="2"/></svg>info@pelicanbuildersllc.com</span>
    </div>
  </header>

  <nav class="nav">
    <a class="active">HOME</a><a>ABOUT</a><a>WHAT WE DO</a><a>PROJECT</a><a>CONTACT</a>
    <div class="search">Search here... <svg width="10" height="10" viewBox="0 0 10 10"><circle cx="4" cy="4" r="3" fill="none" stroke="#1d5ea8" stroke-width="1.3"/><path d="M6.3 6.3L9 9" stroke="#1d5ea8" stroke-width="1.3"/></svg></div>
  </nav>

  <div class="hero" role="img" aria-label="Photo of a bright remodelled kitchen with island and bar stools"></div>
  <div class="dots"><i></i><i></i><i></i><i></i></div>

  <h2 class="section-title">What We Do</h2>

  <div class="service" style="left:56px">
    <div class="photo" role="img" aria-label="Photo of a finished living room interior" style="background:linear-gradient(135deg,#d9d6d0,#8a8378)"></div>
    <h3>Lorem Ipsum is simply</h3>
    <p>Lorem Ipsum is simply dummy text of the printing and typesetting industry. Lorem Ipsum has been the industry.</p>
  </div>
  <div class="service" style="left:276px">
    <div class="photo" role="img" aria-label="Photo of a handyman using a power drill" style="background:linear-gradient(135deg,#f1ece6,#c9562e 60%,#7a4a36)"></div>
    <h3>Lorem Ipsum is simply</h3>
    <p>Lorem Ipsum is simply dummy text of the printing and typesetting industry. Lorem Ipsum has been the industry.</p>
  </div>
  <div class="service" style="left:496px">
    <div class="photo" role="img" aria-label="Photo of a wooden backyard deck with trees" style="background:linear-gradient(135deg,#4f7a33,#9c6a3f 60%,#c79a6b)"></div>
    <h3>Lorem Ipsum is simply</h3>
    <p>Lorem Ipsum is simply dummy text of the printing and typesetting industry. Lorem Ipsum has been the industry.</p>
  </div>

  <section class="welcome">
    <h2>Welcome to PELICAN BUILDERS LLC</h2>
    <div class="mascot" role="img" aria-label="Company mascot character holding a hammer"></div>
    <p class="intro">Lorem Ipsum is simply dummy text of the printing and typesetting industry. Lorem Ipsum has been the industry's standard dummy text ever since the 1500s, when an unknown printer took a galley of type and scrambled it to make a type specimen book. It has survived not only five centuries.</p>
    <ul class="checks">
      <li><svg width="11" height="11" viewBox="0 0 11 11"><rect width="11" height="11" fill="#1d5ea8"/><path d="M2.5 5.5l2 2 4-4" stroke="#fff" stroke-width="1.5" fill="none"/></svg>Lorem Ipsum</li>
      <li><svg width="11" height="11" viewBox="0 0 11 11"><rect width="11" height="11" fill="#1d5ea8"/><path d="M2.5 5.5l2 2 4-4" stroke="#fff" stroke-width="1.5" fill="none"/></svg>Lorem Ipsum</li>
      <li><svg width="11" height="11" viewBox="0 0 11 11"><rect width="11" height="11" fill="#1d5ea8"/><path d="M2.5 5.5l2 2 4-4" stroke="#fff" stroke-width="1.5" fill="none"/></svg>Lorem Ipsum</li>
      <li><svg width="11" height="11" viewBox="0 0 11 11"><rect width="11" height="11" fill="#1d5ea8"/><path d="M2.5 5.5l2 2 4-4" stroke="#fff" stroke-width="1.5" fill="none"/></svg>Lorem Ipsum</li>
      <li><svg width="11" height="11" viewBox="0 0 11 11"><rect width="11" height="11" fill="#1d5ea8"/><path d="M2.5 5.5l2 2 4-4" stroke="#fff" stroke-width="1.5" fill="none"/></svg>Lorem Ipsum</li>
      <li><svg width="11" height="11" viewBox="0 0 11 11"><rect width="11" height="11" fill="#1d5ea8"/><path d="M2.5 5.5l2 2 4-4" stroke="#fff" stroke-width="1.5" fill="none"/></svg>Lorem Ipsum</li>
    </ul>
    <span class="read-more">READ MORE</span>
  </section>

  <aside class="quote">
    <h4>CALL US NOW FOR A<b>FREE QUOTE</b></h4>
    <div class="field">Enter Name</div>
    <div class="field">Enter Email</div>
    <div class="field">Enter Contact No</div>
    <div class="field tall">Enter Message</div>
    <span class="submit">SUBMIT</span>
  </aside>

  <footer class="footer">
    <div class="footer-nav"><span class="pill">Home</span><span>About</span><span>What We Do</span><span>Project</span><span>Contact</span></div>
    <div class="social">
      <svg width="12" height="12" viewBox="0 0 12 12"><circle cx="6" cy="6" r="5" fill="#fff"/></svg>
      <svg width="12" height="12" viewBox="0 0 12 12"><circle cx="6" cy="6" r="5" fill="#fff"/></svg>
      <svg width="12" height="12" viewBox="0 0 12 12"><circle cx="6" cy="6" r="5" fill="#fff"/></svg>
    </div>
    <div class="footer-rule"></div>
    <h5>Contact Us</h5>
    <div class="footer-row">
      <span class="item"><span class="ico"><svg width="10" height="12" viewBox="0 0 10 12"><path d="M5 0a4 4 0 0 0-4 4c0 3 4 8 4 8s4-5 4-8a4 4 0 0 0-4-4z" fill="#1d5ea8"/></svg></span>Lorem Ipsum is simply dummy<br>text of the printing and</span>
      <span class="item"><span class="ico"><svg width="10" height="10" viewBox="0 0 24 24"><path fill="#1d5ea8" d="M6.6 10.8a15 15 0 0 0 6.6 6.6l2.2-2.2c.3-.3.7-.4 1-.2 1.1.4 2.3.6 3.6.6.6 0 1 .4 1 1V20c0 .6-.4 1-1 1A17 17 0 0 1 3 4c0-.6.4-1 1-1h3.5c.6 0 1 .4 1 1 0 1.3.2 2.5.6 3.6.1.3 0 .7-.2 1z"/></svg></span>Call : 123 456 789</span>
      <span class="item"><span class="ico"><svg width="10" height="10" viewBox="0 0 10 10"><rect x="1" y="2" width="8" height="6" fill="#1d5ea8"/></svg></span>Fax : 123 456 789</span>
      <span class="item copy">© PELICAN BUILDERS LLC - 2015, All Rights Reserved</span>
    </div>
  </footer>
</div>
</body>
</html>
```